Velora "Glass Tide" single cover

We need a cover for Velora's New upcoming single "Glass Tide"
We have posted some Pictures and logo that we want you to work With. We need you to get her to look good :).The title is "Glass Tide" and is "Velora feat. Dorvo mint rascal"
The songs is a little hiphop/RnB (Marla Q'ish).
You can choose what colour you want for the logo and overall. But we don't want it to be gloomy.
watch www.velora-music.example or www.facebook.com/veloramusic
This is a digital release so we need only front page 12x12cm
Updates
If anyone wants to remove the background from the pictures and be creative that is fine! :)
Industry/Entity Type
Digital
Colors
Designer to choose colors to be used in the design.
Look and feel
Each slider illustrates characteristics of the customer's brand and the style your logo design should communicate.

```html
<!DOCTYPE html>
<html lang="en">
<head>
<meta charset="utf-8">
<title>Velora – Glass Tide</title>
<link rel="stylesheet" href="https://fonts.googleapis.com/css2?family=Lexend:wght@300;500&display=swap">
<style>
  :root {
    --orange: #f47b2b;
    --orange-light: #f89a3c;
    --pink: #e8357b;
    --hair-dark: #4a2a1c;
    --hair-mid: #8a5a40;
    --hair-light: #a97658;
    --skin-light: #f0c6ae;
    --skin-mid: #e0a68c;
    --skin-warm: #d58f76;
  }
  html, body {
    margin: 0;
    padding: 0;
    width: 1200px;
    height: 1200px;
    overflow: hidden;
    background: var(--hair-mid);
  }
  .cover {
    position: relative;
    width: 1200px;
    height: 1200px;
    overflow: hidden;
    font-family: "Lexend", sans-serif;
  }
  .cover-photo {
    position: absolute;
    inset: 0;
    background:
      radial-gradient(ellipse 520px 640px at 850px 620px, var(--skin-light) 0%, var(--skin-mid) 40%, rgba(213,143,118,0.55) 68%, rgba(213,143,118,0) 100%),
      radial-gradient(ellipse 300px 360px at 1150px 120px, rgba(240,198,174,0.8) 0%, rgba(240,198,174,0) 100%),
      radial-gradient(ellipse 260px 420px at 1160px 900px, rgba(74,42,28,0.7) 0%, rgba(74,42,28,0) 100%),
      radial-gradient(ellipse 520px 800px at 260px 520px, var(--hair-light) 0%, var(--hair-mid) 55%, var(--hair-dark) 100%);
  }
  .title-stack {
    position: absolute;
    inset: 0;
  }
  .title-stack text {
    font-family: "Lexend", sans-serif;
    text-transform: uppercase;
  }
  .line-artist, .line-title { fill: url(#orange-fill); }
  .line-featured { fill: var(--pink); }
  .line-light { font-weight: 300; }
  .line-bold { font-weight: 500; }
  .brand-name {
    position: absolute;
    right: 54px;
    bottom: 72px;
    margin: 0;
    font-size: 60px;
    font-weight: 500;
    line-height: 1;
    color: var(--orange);
    letter-spacing: 2px;
  }
</style>
</head>
<body>
  <main class="cover">
    <div class="cover-photo" role="img" aria-label="Close-up portrait photo of the singer with long wavy brown hair, smiling warmly, filling the whole cover"></div>

    <svg class="title-stack" width="1200" height="1200" viewBox="0 0 1200 1200" aria-label="Velora feat Dorvo mint rascal – Glass Tide">
      <defs>
        <linearGradient id="orange-fill" x1="0" y1="0" x2="1" y2="1">
          <stop offset="0" stop-color="var(--orange)"/>
          <stop offset="0.5" stop-color="var(--orange-light)"/>
          <stop offset="1" stop-color="var(--orange)"/>
        </linearGradient>
      </defs>
      <text class="line-artist line-light" x="108" y="160" font-size="150" textLength="490" lengthAdjust="spacingAndGlyphs">Velora</text>
      <text class="line-artist line-bold" x="108" y="335" font-size="228" textLength="490" lengthAdjust="spacingAndGlyphs">Feat</text>
      <text class="line-featured line-light" x="108" y="440" font-size="114" textLength="490" lengthAdjust="spacingAndGlyphs">Dorvo</text>
      <text class="line-featured line-bold" x="108" y="645" font-size="264" textLength="490" lengthAdjust="spacingAndGlyphs">Mint</text>
      <text class="line-featured line-light" x="108" y="770" font-size="121" textLength="490" lengthAdjust="spacingAndGlyphs">Rascal</text>
      <text class="line-title line-light" x="108" y="935" font-size="207" textLength="490" lengthAdjust="spacingAndGlyphs">Glass</text>
      <text class="line-title line-light" x="108" y="1110" font-size="207" textLength="490" lengthAdjust="spacingAndGlyphs">Tide</text>
    </svg>

    <p class="brand-name">velora</p>
  </main>
</body>
</html>
```